Medical supplies company needs a catalogue re-design

Our present catalogue is spread over a number of pages but this needs to be reduced. 4-5 images would require to be on each page. It needs to be professional, simple and elegant. The photos and descriptors need to be adjacent to each other. It should be able to be emailed conventionally as an e-catalogue without it being compressed. an email with existing catalogue will be emailed to anyone interested.
https://www.quillvault.net/s/81tazup7rqwmdlon/consumables%20photos%20and%20descriptions.pdf?dl=0
Target Market(s)
medical practices, hospitals
Industry/Entity Type
Medical Supply

```html
<!DOCTYPE html>
<html lang="en">
<head>
<meta charset="utf-8">
<title>Wound Care – Velora Care Catalogue</title>
<link rel="stylesheet" href="https://fonts.googleapis.com/css2?family=Arimo:wght@400;700&display=swap">
<style>
  :root {
    --brand-red: #d7262e;
    --ink: #2b2b2b;
    --body-ink: #3a3a3a;
    --panel: #e6e6e7;
    --panel-edge: #6a6b6e;
    --paper: #ffffff;
    --muted: #555555;
  }
  * { box-sizing: border-box; margin: 0; padding: 0; }
  html, body { width: 929px; height: 1200px; overflow: hidden; background: var(--paper); }
  body { font-family: "Arimo", Arial, sans-serif; color: var(--body-ink); }
  .page { position: relative; width: 929px; height: 1200px; overflow: hidden; background: var(--paper); }

  .band { position: absolute; left: 0; width: 100%; background: var(--brand-red); }
  .band--top { top: 0; height: 30px; }
  .band--bottom { bottom: 0; height: 41px; }

  .section-title {
    position: absolute; left: 61px; top: 62px;
    font-size: 40px; font-weight: 400; color: var(--brand-red);
    font-variant: small-caps; letter-spacing: 1px; line-height: 1.1;
  }

  .product {
    position: absolute;
    background: var(--panel);
    border: 1.5px solid var(--panel-edge);
    border-radius: 16px;
    box-shadow: 2px 3px 4px rgba(0,0,0,0.25);
  }
  .product__body { position: absolute; font-size: 14.5px; line-height: 1.28; }
  .product__name { font-size: 17px; font-weight: 400; color: var(--ink); line-height: 1.2; margin-bottom: 2px; }
  .product__lead { color: var(--body-ink); }
  .product__list { list-style: none; }
  .product__list li { position: relative; padding-left: 11px; }
  .product__list li::before { content: "•"; position: absolute; left: 0; }
  .product__list--numbered { list-style: decimal; padding-left: 20px; }
  .product__list--numbered li { padding-left: 2px; }
  .product__list--numbered li::before { content: none; }
  .is-red { color: var(--brand-red); }

  .photo { position: absolute; border-radius: 4px; }

  .brand { position: absolute; left: 677px; top: 1030px; display: flex; align-items: center; gap: 10px; white-space: nowrap; }
  .brand__name { font-size: 25px; font-weight: 700; color: var(--brand-red); letter-spacing: 2px; line-height: 1; }
  .brand__mark { width: 22px; height: 22px; border-radius: 50%; background: var(--brand-red); flex: none; }
  .brand__url { position: absolute; left: 667px; top: 1094px; font-size: 14px; color: var(--muted); letter-spacing: 1.5px; white-space: nowrap; }
</style>
</head>
<body>
<main class="page">
  <div class="band band--top"></div>

  <h1 class="section-title">Wound Care</h1>

  <!-- Nonwoven tape -->
  <section class="product" style="left:174px; top:153px; width:429px; height:165px;">
    <div class="product__body" style="left:56px; top:16px; width:200px;">
      <h2 class="product__name">High Quality<br>Nonwoven Tape</h2>
      <ul class="product__list is-red">
        <li>Non-allergenic and suitable for the most sensitive and soft skin.</li>
        <li>Box of 10</li>
      </ul>
    </div>
  </section>
  <div class="photo" role="img" aria-label="Roll of white nonwoven medical tape" style="left:56px; top:164px; width:123px; height:106px; background:radial-gradient(circle at 45% 50%, #ffffff 30%, #dfe6ee 70%, #b9c6d4 100%);"></div>

  <!-- Wound closure strips -->
  <section class="product" style="left:626px; top:144px; width:256px; height:318px;">
    <div class="product__body" style="left:48px; top:20px; width:196px;">
      <h2 class="product__name">Wound Closure<br>Strips</h2>
      <ul class="product__list is-red">
        <li>Reinforced strips of microporous material for fast and effective wound closure or to be applied to wounds that have been stitched to provide extra tensile support.</li>
        <li>3mm by 75mm (five pcs per package, 50 packages in a box)</li>
        <li>6mm by 75mm (three pcs per package, 50 packages in a box)</li>
      </ul>
    </div>
  </section>
  <div class="photo" role="img" aria-label="Box of wound closure strips with a sample packet" style="left:462px; top:165px; width:150px; height:103px; background:linear-gradient(160deg, #f4f6fa 0%, #dfe4ee 55%, #3f55a0 100%);"></div>

  <!-- Film island dressing -->
  <section class="product" style="left:174px; top:336px; width:437px; height:276px;">
    <div class="product__body" style="left:138px; top:18px; width:288px;">
      <h2 class="product__name">Film Island Dressing with Pad</h2>
      <p class="product__lead">Waterproof dressings with a pad to absorb wound exudate. These are used following surgical procedures to cover wounds to prevent infection.</p>
      <ol class="product__list product__list--numbered is-red">
        <li>Made of transparent PU film with gauze pad in the centre 2. Acts as a barrier to bacteria, debris and water 3. 50 pcs per box</li>
        <li>Sizes: 6cm by 7cm, 7cm by 10cm, 10cm by 12cm, 10cm by 15cm, 10cm by 20cm</li>
      </ol>
    </div>
  </section>
  <div class="photo" role="img" aria-label="Packaged transparent film dressing" style="left:56px; top:349px; width:227px; height:159px; background:linear-gradient(170deg, #fbfbfb 0%, #e9efe8 60%, #c9d8c6 100%);"></div>
  <div class="photo" role="img" aria-label="Film island dressing with centre pad" style="left:79px; top:523px; width:197px; height:110px; border-radius:18px; background:radial-gradient(ellipse at 50% 50%, #e2b99a 0 20%, #f2f2f2 22%, #dcdcdc 100%);"></div>

  <!-- Crepe bandages -->
  <section class="product" style="left:56px; top:658px; width:555px; height:160px;">
    <div class="product__body" style="left:30px; top:14px; width:250px;">
      <h2 class="product__name">Unbleached Crepe Elastic</h2>
      <p class="product__lead">Bandages (7.5 cm x 4.5 m, 10cm x 4.5 m)</p>
      <ul class="product__list">
        <li>Ideal for holding dressings in place</li>
        <li>can be used for strapping</li>
      </ul>
      <p class="is-red">&nbsp;&nbsp;(12 rolls per box)</p>
    </div>
  </section>
  <div class="photo" role="img" aria-label="Three wrapped crepe bandage rolls" style="left:368px; top:671px; width:235px; height:131px; background:linear-gradient(180deg, #f7f5ee 0%, #e6e1d2 60%, #cfc8b4 100%);"></div>

  <!-- Skin colour high elastic -->
  <section class="product" style="left:626px; top:561px; width:256px; height:424px;">
    <div class="product__body" style="left:6px; top:186px; width:244px;">
      <h2 class="product__name">Skin Colour High Elastic</h2>
      <p class="product__lead">Bandages (7.5 cm x 4.5 m, 10cm x 4.5 m)</p>
      <ul class="product__list">
        <li>ideal for treatment, after-care &amp; prevention of sports injuries</li>
        <li>secured with lightweight metal clips</li>
        <li>knit design offers strength, comfort &amp; breathability</li>
        <li>individually wrapped</li>
      </ul>
      <p class="is-red">&nbsp;&nbsp;(12 rolls per box)</p>
    </div>
  </section>
  <div class="photo" role="img" aria-label="Two wrapped skin colour elastic bandage rolls" style="left:644px; top:477px; width:232px; height:232px; background:linear-gradient(180deg, #e9c7b5 0%, #d9a892 50%, #c99480 100%);"></div>

  <!-- Cohesive bandages -->
  <section class="product" style="left:174px; top:862px; width:437px; height:225px;">
    <div class="product__body" style="left:155px; top:24px; width:268px;">
      <h2 class="product__name">Cohesive Bandages (7.5 cm x 4.5 m, 10cm x 4.5 m)</h2>
      <ul class="product__list is-red">
        <li>offers compression to support a joint or muscle</li>
        <li>secures wound dressings &amp; is painless when removed</li>
        <li>secures to itself &amp; can be torn by hand</li>
        <li>won't leave any sticky residue</li>
        <li>conforms to all body contours</li>
      </ul>
    </div>
  </section>
  <div class="photo" role="img" aria-label="Red cohesive bandage roll" style="left:56px; top:879px; width:262px; height:182px; border-radius:40px; background:radial-gradient(ellipse at 40% 45%, #f04a52 0%, #d8202c 55%, #a8121b 100%);"></div>

  <div class="brand">
    <span class="brand__name">VELORA CARE</span>
    <span class="brand__mark"></span>
  </div>
  <p class="brand__url">www.veloracare.com.au</p>

  <div class="band band--bottom"></div>
</main>
</body>
</html>
```